Artistic Poster for a Short Film

I am the Writer/Director of an upcoming short film called "Driftwater" and I need a 20x30 poster for the project screening. The screening is coming up very soon so apologies for the quick turnaround time. Here is a short synopsis:

"Walter is a mysterious man who is lost and disoriented. With the help of Marisol, he searches for items out of an old diary written long ago by a woman named Gloria, despite not understanding exactly why he does so. Marisol helps, but when they are unsuccessful she confronts Walter: Does he know why he restlessly searches for these items? The truth is shocking, and reveals Walter's connections to Marisol, Gloria, and the strange old diary.

The truth is that Walter is actually an old man, and Marisol is his caretaker and granddaughter. His memories, including those of Gloria, his deceased wife, have been destroyed by Dementia. He often wakes believing himself to be at an earlier stage of his life, and therefore meets many of the challenges of life with anger and confusion."

Here is the film's website: http://www.driftwater-film.example
Here is our successful Fundbarrow: http://www.fundbarrow.example/projects/502847719/driftwater-a-short-film

The design should be dark and simple. I'm a fan of the art-prints that this short film used (scroll down to see): http://www.fundbarrow.example/projects/ruthvanderlo/kettle-a-short-film-based-on-the-story-by-omar-quill but I'm also open to other ideas. If you google "alternative movie posters" you'll see what I mean. The poster should be simple, easy to read, and hint at the themes of the film without giving the twist away.

Here is a link to the Fine Cut of the film: https://clipvault.example/48210576 The password is: lanterns72
It is not a completed version but will give you an idea of what the film will look like.

Target Market(s)

The intended audience is an art-film crowd of moviegoers.

Industry/Entity Type

Movie

Requirements
Must have
• The poster must have the typical movie poster text at the bottom. The information that should be included is: First line: COPPER LANTERN STUDIOS presents a film by DANIEL OSTROM "DRIFTWATER" MARCEL BRUNAUD TERRA WOLCOTT
Second line: music by OWEN PRATT director of photography VICTOR L. MORALES edited by SIMON ORR costume designer ROBERTA CLINE
Third line: produced by GAIL TORVALD DANIEL OSTROM written and directed by DANIEL OSTROM

It should have the title of the film "Driftwater" and "A film by Daniel Ostrom" on the poster (in addition to the text at the bottom.

It must be high-quality and printable to a size of 20x30. Ideal resolution is 6060x9090. I only need the high quality printable file, I will do the printing myself.
Should not have
• Bright colors.

```html
<!DOCTYPE html>
<html lang="en">
<head>
<meta charset="utf-8">
<title>Driftwater — Poster</title>
<link rel="stylesheet" href="https://fonts.googleapis.com/css2?family=Cabin:wght@400;500&family=Oswald:wght@400;500&display=swap">
<style>
  :root {
    --bg-light: #5e5c38;
    --bg-mid: #3d3c26;
    --bg-dark: #1c1b11;
    --figure-warm: #8a5f22;
    --figure-shadow: #050505;
    --figure-grey: #55564a;
    --title: #b9b287;
    --byline: #f1eac2;
    --credit: #d9d4b6;
  }
  * { margin: 0; padding: 0; box-sizing: border-box; }
  html, body { width: 800px; height: 1200px; overflow: hidden; background: var(--bg-dark); }
  .poster {
    position: relative;
    width: 800px;
    height: 1200px;
    overflow: hidden;
    background:
      radial-gradient(ellipse 70% 55% at 62% 38%, var(--bg-light) 0%, var(--bg-mid) 55%, var(--bg-dark) 100%);
  }
  .portrait {
    position: absolute;
    left: 0;
    top: 0;
    width: 800px;
    height: 1200px;
  }
  .title-block {
    position: absolute;
    left: 160px;
    top: 900px;
    width: 540px;
    text-align: right;
  }
  .film-title {
    font-family: 'Cabin', sans-serif;
    font-weight: 500;
    font-size: 78px;
    letter-spacing: 3px;
    color: var(--title);
    line-height: 1;
    text-align: center;
  }
  .byline {
    margin-top: 14px;
    font-family: 'Cabin', sans-serif;
    font-size: 20px;
    letter-spacing: 1px;
    color: var(--byline);
    padding-right: 4px;
  }
  .billing {
    position: absolute;
    left: 0;
    top: 1058px;
    width: 800px;
    font-family: 'Oswald', sans-serif;
    color: var(--credit);
    text-align: center;
  }
  .billing-line {
    display: flex;
    justify-content: center;
    align-items: center;
    gap: 6px;
    white-space: nowrap;
    height: 22px;
    margin-bottom: 8px;
  }
  .name { font-size: 17px; font-weight: 500; line-height: 1; letter-spacing: 0.2px; }
  .role { font-size: 7px; line-height: 1.05; text-transform: uppercase; text-align: right; }
  .role.inline { font-size: 9px; align-self: flex-end; padding-bottom: 2px; }
</style>
</head>
<body>
<main class="poster">
  <svg class="portrait" viewBox="0 0 800 1200" role="img" aria-label="Split portrait of a man's head and shoulders: the left half younger in warm amber tones, the right half aged in black and grey">
    <defs>
      <linearGradient id="warmHalf" x1="0" y1="0" x2="0" y2="1">
        <stop offset="0" stop-color="#6a4718"/>
        <stop offset="0.35" stop-color="var(--figure-warm)"/>
        <stop offset="0.7" stop-color="#2a1c08"/>
        <stop offset="1" stop-color="var(--figure-shadow)"/>
      </linearGradient>
      <linearGradient id="greyHalf" x1="0" y1="0" x2="0" y2="1">
        <stop offset="0" stop-color="#1a1a16"/>
        <stop offset="0.4" stop-color="var(--figure-grey)"/>
        <stop offset="0.7" stop-color="#141411"/>
        <stop offset="1" stop-color="var(--figure-shadow)"/>
      </linearGradient>
    </defs>
    <path d="M372 150 C290 160 220 230 212 340 L212 700 C150 760 110 900 95 1200 L372 1200 Z" fill="url(#warmHalf)"/>
    <path d="M372 150 C470 160 560 240 570 360 L575 640 C680 700 780 760 800 800 L800 1200 L372 1200 Z" fill="url(#greyHalf)"/>
  </svg>

  <header class="title-block">
    <h1 class="film-title">DRIFTWATER</h1>
    <p class="byline">A FILM BY DANIEL OSTROM</p>
  </header>

  <footer class="billing">
    <div class="billing-line">
      <span class="name">COPPER LANTERN STUDIOS</span>
      <span class="role inline">PRESENTS A</span>
      <span class="name">DANIEL OSTROM</span>
      <span class="role inline">A FILM BY</span>
      <span class="name">MARCEL BRUNAUD TERRA WOLCOTT</span>
      <span class="name">"DRIFTWATER"</span>
    </div>
    <div class="billing-line">
      <span class="role">Music<br>by</span><span class="name">OWEN PRATT</span>
      <span class="role">Costume<br>designer</span><span class="name">ROBERTA CLINE</span>
      <span class="role">Edited<br>by</span><span class="name">SIMON ORR</span>
      <span class="role">Production<br>designer</span><span class="name">DESIGNERS NAME</span>
      <span class="role">Director of<br>photography</span><span class="name">VICTOR L. MORALES</span>
    </div>
    <div class="billing-line">
      <span class="role">Produced<br>by</span><span class="name">GAIL TORVALD DANIEL OSTROM</span>
      <span class="role">Story<br>by</span><span class="name">&amp;</span>
      <span class="role">Directed<br>by</span><span class="name">DANIEL OSTROM</span>
    </div>
  </footer>
</main>
</body>
</html>
```